Seed Company Looking For a Soybean Seed Bag Design

We are are a regional seed company who is currently launching a new line of soybean products. The brand of the product will be Tru-Vora. We are looking for a custom design of a soybean bag measuring 16"x5"x30" (when constructed). We are looking for a modern design that's relatively loud, but not too busy. The proof needs to match with the attached template. We have also provided a proof of a previous bag project (Fox-Brook-Standard) we've done to show how the artwork needs to be laid out. In no way does the new design need to resemble the example. Also attached are some other examples of seed bags.
Agriculture
Designer to choose colors to be used in the design.

```html
<!DOCTYPE html>
<html lang="en">
<head>
<meta charset="utf-8">
<title>Tru-Vora Soybean Seed – Bag Layout</title>
<link rel="stylesheet" href="https://fonts.googleapis.com/css2?family=Oswald:wght@200;300;500;700&display=swap">
<style>
  :root {
    --page-bg: #ebfde2;
    --band-green: #8cc63f;
    --title-green: #2ba24c;
    --brand-grey: #6d6e71;
    --panel-white: #ffffff;
    --fold-line: #c9c9c9;
  }
  html, body {
    margin: 0;
    padding: 0;
    width: 1200px;
    height: 1200px;
    overflow: hidden;
    background: var(--page-bg);
  }
  .canvas {
    position: relative;
    width: 1200px;
    height: 1200px;
    display: flex;
    align-items: center;
    justify-content: center;
  }
  .bag-layout {
    width: 1080px;
    height: 843px;
    filter: drop-shadow(0 3px 6px rgba(0,0,0,0.18));
  }
  .panel { fill: var(--panel-white); }
  .fold { stroke: var(--fold-line); stroke-width: 1; }
  .band { fill: var(--band-green); }
  .title-bold {
    font-family: "Oswald", sans-serif;
    font-weight: 700;
    fill: var(--title-green);
  }
  .title-light {
    font-family: "Oswald", sans-serif;
    font-weight: 200;
    fill: var(--title-green);
  }
  .brand-small {
    font-family: "Oswald", sans-serif;
    font-weight: 500;
    fill: var(--brand-grey);
    letter-spacing: 1px;
  }
  .brand-name {
    font-family: "Oswald", sans-serif;
    font-weight: 500;
    fill: var(--title-green);
    letter-spacing: 1px;
  }
  .brand-square { fill: var(--title-green); }
</style>
</head>
<body>
<main class="canvas">
  <svg class="bag-layout" viewBox="0 0 856 668" xmlns="http://www.w3.org/2000/svg" aria-label="Tru-Vora soybean seed bag, flat panel layout">
    <!-- Side panel A -->
    <g class="side-panel side-panel-a">
      <rect class="panel" x="0" y="0" width="117" height="668"/>
      <rect class="band" x="0" y="0" width="117" height="27"/>
      <rect class="band" x="0" y="640" width="117" height="28"/>
      <text class="title-bold" transform="translate(13,118) rotate(90)" font-size="80" textLength="270" lengthAdjust="spacingAndGlyphs">SOYBEAN</text>
      <text class="title-light" transform="translate(13,400) rotate(90)" font-size="80" textLength="150" lengthAdjust="spacingAndGlyphs">SEED</text>
      <text class="brand-small" transform="translate(85,252) rotate(90)" font-size="22" textLength="136" lengthAdjust="spacingAndGlyphs">TRU-VORA</text>
    </g>

    <!-- Front panel -->
    <g class="front-panel">
      <rect class="panel" x="117" y="0" width="375" height="668"/>
      <polygon class="band" points="117,0 492,0 117,181"/>
      <polygon class="band" points="117,668 492,470 492,668"/>
      <g class="brand-lockup">
        <rect class="brand-square" x="230" y="205" width="14" height="14"/>
        <text class="brand-name" x="252" y="220" font-size="22" textLength="120" lengthAdjust="spacingAndGlyphs">TRU-VORA</text>
      </g>
      <text class="title-bold" x="135" y="381" font-size="96" textLength="338" lengthAdjust="spacingAndGlyphs">SOYBEAN</text>
      <text class="title-light" x="218" y="492" font-size="108" textLength="170" lengthAdjust="spacingAndGlyphs">SEED</text>
    </g>

    <!-- Side panel B -->
    <g class="side-panel side-panel-b">
      <rect class="panel" x="492" y="0" width="117" height="668"/>
      <rect class="band" x="492" y="0" width="117" height="28"/>
      <rect class="band" x="492" y="640" width="117" height="28"/>
      <text class="title-bold" transform="translate(596,553) rotate(-90)" font-size="82" textLength="275" lengthAdjust="spacingAndGlyphs">SOYBEAN</text>
      <text class="title-light" transform="translate(596,266) rotate(-90)" font-size="80" textLength="148" lengthAdjust="spacingAndGlyphs">SEED</text>
      <text class="brand-small" transform="translate(522,408) rotate(-90)" font-size="22" textLength="140" lengthAdjust="spacingAndGlyphs">TRU-VORA</text>
    </g>

    <!-- Back panel -->
    <g class="back-panel">
      <rect class="panel" x="609" y="0" width="247" height="668"/>
      <polygon class="band" points="609,0 856,0 856,184"/>
      <polygon class="band" points="609,490 609,668 856,668"/>
    </g>

    <!-- Fold lines -->
    <line class="fold" x1="117" y1="0" x2="117" y2="668"/>
    <line class="fold" x1="492" y1="0" x2="492" y2="668"/>
    <line class="fold" x1="609" y1="0" x2="609" y2="668"/>
  </svg>
</main>
</body>
</html>
```